KORVO RENEWABLES

New business B2B Energy Renewables website.
Please refer to our competitor https://www.tarnex42.co.uk/ for a similar website.

Need extra days to review

```html
<!DOCTYPE html>
<html lang="en">
<head>
<meta charset="utf-8">
<title>KORVO RENEWABLES</title>
<link href="https://fonts.googleapis.com/css2?family=Poppins:ital,wght@0,400;0,500;0,600;0,700;1,400&display=swap" rel="stylesheet">
<style>
:root{
  --blue:#1f78e6;
  --blue-deep:#0d4fb8;
  --blue-dark:#0a3f99;
  --navy:#0c2a4f;
  --ink:#2d2d2d;
  --muted:#666;
  --grey:#ececec;
  --white:#fff;
}
*{margin:0;padding:0;box-sizing:border-box}
html,body{width:1200px;height:4062px;overflow:hidden}
body{font-family:"Poppins",sans-serif;color:var(--ink);background:var(--white);position:relative}
.abs{position:absolute}
.btn{position:absolute;display:flex;align-items:center;justify-content:center;background:linear-gradient(180deg,var(--blue),var(--blue-deep));color:var(--white);font-weight:600;border-radius:22px;letter-spacing:.3px}
.site-header{position:absolute;left:0;top:0;width:1200px;height:140px;background:var(--white);z-index:3}
.call{left:103px;top:34px;font-size:15px;font-weight:600;color:var(--blue);display:flex;align-items:center;gap:8px}
.nav a{position:absolute;top:88px;font-size:16px;font-weight:600;color:#111;text-decoration:none}
.nav a.active{color:var(--blue);font-weight:500}
.brand-tab{left:448px;top:100px;width:304px;height:52px;background:var(--white);border-radius:0 0 40px 40px;z-index:2}
.brand{left:470px;top:52px;width:260px;text-align:center;font-size:22px;font-weight:700;color:var(--navy);z-index:4;display:flex;align-items:center;justify-content:center;gap:10px}
.brand i{width:14px;height:14px;background:var(--blue);display:inline-block}
.hero{left:0;top:140px;width:1200px;height:612px;background:linear-gradient(180deg,#f0b383 0%,#b9a5ad 22%,#4a73c4 42%,#2757ad 70%,#1c3f86 100%)}
.hero-title{left:0;top:385px;width:1200px;text-align:center;font-size:50px;font-weight:700;color:var(--white)}
.hero .cta,.hero-cta{left:504px;top:470px;width:188px;height:48px;border:2px solid var(--white);font-size:18px;background:var(--blue-deep)}
.h2{position:absolute;left:0;width:1200px;text-align:center;font-weight:700;font-size:44px;color:#333}
.sub{position:absolute;left:260px;width:680px;text-align:center;font-style:italic;font-size:20px;line-height:24px;color:#555}
.about-art{left:71px;top:1009px;width:686px;height:284px;background:linear-gradient(135deg,#2f6fd0,#0d3d96);clip-path:polygon(0 0,54% 0,54% 0,100% 100%,16% 100%)}
.about-text{left:680px;top:1009px;width:397px;text-align:right;font-size:16.5px;line-height:20px;color:#555}
.services{left:0;top:1415px;width:1200px;height:816px;background:linear-gradient(160deg,#2a86f2 0%,#1664d4 45%,#0e4fb6 100%);clip-path:polygon(0 0,56% 4%,100% 2%,100% 97%,0 100%)}
.svc-title{left:0;top:1500px;width:1200px;text-align:center;color:var(--white);font-size:46px;font-weight:700}
.svc{position:absolute;color:var(--white);width:270px}
.svc h3{font-size:23px;font-weight:700;margin-bottom:4px}
.svc p{font-size:15px;line-height:18px}
.svc.right{text-align:right}
.testi-card{left:295px;top:2496px;width:646px;height:343px;background:var(--white);box-shadow:0 8px 40px rgba(0,0,0,.12);clip-path:polygon(0 0,100% 0,100% 100%,3% 100%)}
.testi-edge{left:258px;top:2498px}
.quote-mark{left:296px;top:2440px;font-size:150px;font-weight:700;color:#666;line-height:1}
.testi-text{left:320px;top:2572px;width:560px;text-align:center;font-style:italic;font-size:16.5px;line-height:27px;color:#666}
.testi-name{left:0;top:2760px;width:1200px;text-align:center;color:var(--blue);font-weight:600;font-size:16px}
.solutions{left:0;top:2955px;width:1200px;height:720px;background:var(--grey)}
.card{position:absolute;top:3170px;width:279px;height:370px;background:var(--white);border-radius:0 0 60px 0;overflow:hidden}
.card .ph{height:169px}
.card h4{margin:22px 30px 0;font-size:20px;line-height:24px;font-weight:600;color:#333;height:56px}
.card p{margin:10px 30px 0;font-size:14px;line-height:17px;color:#777}
.card .btn{left:34px;top:300px;width:124px;height:40px;font-size:15px}
.footer{left:0;top:3651px;width:1200px;height:411px;background:linear-gradient(180deg,#0b3c7c,#0b2b52);clip-path:polygon(0 6%,100% 0,100% 100%,0 100%)}
.f-h{position:absolute;top:3762px;color:var(--white);font-size:25px;font-weight:700}
.f-item{position:absolute;left:150px;display:flex;align-items:center;gap:20px;color:var(--white);font-size:16px;line-height:22px}
.f-ic{width:46px;height:46px;border-radius:50%;background:var(--blue);display:flex;align-items:center;justify-content:center}
.f-links{left:494px;top:3832px;color:var(--white);font-size:16px;line-height:23.5px}
.f-brand{left:770px;top:3800px;width:270px;text-align:center;color:var(--white);font-size:24px;font-weight:700}
.socials{left:836px;top:3896px;display:flex;gap:24px}
.socials span{width:24px;height:24px;border-radius:50%;background:var(--white)}
.copy{left:760px;top:3958px;width:300px;text-align:center;color:var(--white);font-size:16px}
</style>
</head>
<body>

<header class="site-header">
  <div class="abs call">
    <svg width="16" height="16" viewBox="0 0 24 24"><path fill="#1f78e6" d="M6.6 10.8a15 15 0 0 0 6.6 6.6l2.2-2.2c.3-.3.7-.4 1-.2 1.1.4 2.3.6 3.6.6.6 0 1 .4 1 1V20c0 .6-.4 1-1 1A17 17 0 0 1 3 4c0-.6.4-1 1-1h3.5c.6 0 1 .4 1 1 0 1.3.2 2.5.6 3.6.1.3 0 .7-.2 1z"/></svg>
    CALL : 555 014 3372
  </div>
  <nav class="nav">
    <a class="active" style="left:106px">HOME</a>
    <a style="left:199px">ABOUT US</a>
    <a style="left:333px">SERVICES</a>
    <a style="left:766px">RENEWABLE SOLUTIONS</a>
    <a style="left:1007px">CONTACT US</a>
  </nav>
  <div class="btn" style="left:988px;top:25px;width:140px;height:37px;font-size:14px">GET A QUOTE</div>
</header>
<div class="abs brand-tab"></div>
<div class="abs brand"><i></i>KORVO RENEWABLES</div>

<section>
  <div class="abs hero" role="img" aria-label="Solar panel field with wind turbines at sunset"></div>
  <svg class="abs" style="left:0;top:680px" width="1200" height="80" viewBox="0 0 1200 80">
    <polygon points="0,72 420,52 1200,12 1200,70" fill="#1a62d0"/>
    <polygon points="0,80 420,52 1200,70 1200,80" fill="#fff"/>
  </svg>
  <h1 class="abs hero-title">KORVO RENEWABLES</h1>
  <div class="btn hero-cta">GET A QUOTE</div>
</section>

<section>
  <h2 class="h2" style="top:818px">ABOUT KORVO RENEWABLES</h2>
  <p class="sub" style="top:894px">Lorem ipsum dolor sit amet, consectetur adipiscing elit, sed do eiusmod tempor incididunt ut let dolore magna aliqua.</p>
  <div class="abs about-art" role="img" aria-label="Illustration of tilted solar panel arrays"></div>
  <p class="abs about-text">Lorem ipsum dolor sit amet, consectetur adipi scing elit, sed do eiusmod tempor incididunt ut labore et dolore magna ali uis ipsum suspend isse ultrices gravida. loreisus commodo viverra mae cenas Lorem ipsum dolor sit amet, con sectetlour adipiscing elit, sed do eiusmod por incididunt ut labore et dolore magna ali uis ium suspendisse ultrices gravida. .loreisus commodo viverra ma</p>
  <div class="btn" style="left:891px;top:1207px;width:186px;height:50px;font-size:18px">READ MORE</div>
</section>

<section>
  <div class="abs services"></div>
  <h2 class="abs svc-title">OUR SERVICES</h2>
  <svg class="abs" style="left:380px;top:1620px" width="440" height="440" viewBox="0 0 440 440">
    <circle cx="220" cy="225" r="186" fill="#0f4fb0" stroke="#3f8ef0" stroke-width="6"/>
    <circle cx="220" cy="225" r="70" fill="#1f78e6"/>
    <g fill="#1a6ee0" stroke="#fff" stroke-width="4">
      <circle cx="87" cy="75" r="55"/><circle cx="341" cy="75" r="55"/>
      <circle cx="65" cy="249" r="55"/><circle cx="379" cy="257" r="55"/>
      <circle cx="220" cy="367" r="55"/>
    </g>
    <g fill="none" stroke="#fff" stroke-width="2.5">
      <circle cx="75" cy="68" r="8"/><circle cx="99" cy="68" r="8"/><path d="M60 95q15-18 30 0M84 95q15-18 30 0"/>
      <circle cx="341" cy="75" r="20"/><path d="M333 75l6 6 10-12"/>
      <path d="M48 265l30-30 8 8-30 30zM50 236l28 28"/>
      <path d="M360 250h16v20h-16zM376 254h18l4 12h-22"/>
      <circle cx="212" cy="372" r="14"/><path d="M212 364v16M226 358h14v26h-14"/>
    </g>
  </svg>
  <div class="svc right" style="left:120px;top:1635px"><h3>CONSULTING</h3><p>Lorem ipsum dolor sit amet, con sectetur adipi scing elit, sed do eiusmod tempor incid.</p></div>
  <div class="svc" style="left:801px;top:1635px"><h3>MAINTENANCE</h3><p>Lorem ipsum dolor sit amet, con sectetur adipi scing elit, sed do eiusmod tempor incid.</p></div>
  <div class="svc right" style="left:96px;top:1807px"><h3>DESIGN</h3><p>Lorem ipsum dolor sit amet, con sectetur adipi scing elit, sed do eiusmod tempor incid.</p></div>
  <div class="svc" style="left:839px;top:1814px"><h3>INSTALLATION</h3><p>Lorem ipsum dolor sit amet, con sectetur adipi scing elit, sed do eiusmod tempor incid.</p></div>
  <div class="svc" style="left:420px;top:2070px;width:360px;text-align:center"><h3>FINANCE</h3><p>Lorem ipsum dolor sit amet, con sectetur adipi scing elit, sed do eiusmod tempor incid.</p></div>
</section>

<section>
  <h2 class="h2" style="top:2305px">TESTIMONIALS</h2>
  <p class="sub" style="top:2380px">Lorem ipsum dolor sit amet, consectetur adipiscing elit, sed do eiusmod tempor incididunt ut let dolore magna aliqua.</p>
  <svg class="abs testi-edge" width="350" height="350" viewBox="0 0 350 350">
    <polyline points="2,0 38,338 345,338" fill="none" stroke="#1f78e6" stroke-width="7"/>
  </svg>
  <div class="abs testi-card"></div>
  <div class="abs quote-mark">“</div>
  <p class="abs testi-text">“Lorem ipsum dolor sit amet, consectetur adipi scing elit,eiu smod tempor incididunt ut labore et dolore magna ali uis ipsum suspend isse ultrices gravida. loreisus commodo viverra mae cenas Lorem ipsum dolor sit amet, con sectetlour adipiscing elit, sed do eiusmod &nbsp;por incididunt ut labore et dolor”</p>
  <div class="abs testi-name">TOMAS REDLAND</div>
</section>

<section>
  <div class="abs solutions"></div>
  <svg class="abs" style="left:0;top:2955px" width="1200" height="50" viewBox="0 0 1200 50">
    <polygon points="0,0 1200,0 1200,-8 520,28 0,12" fill="#fff"/>
    <polygon points="520,28 1200,-8 1200,48" fill="#1457c4"/>
  </svg>
  <h2 class="h2" style="top:3068px">RENEWABLE SOLUTIONS</h2>
  <article class="card" style="left:150px">
    <div class="ph" role="img" aria-label="Solar panels under a bright sky" style="background:linear-gradient(180deg,#7ea6d6,#e8d9a0 55%,#3b5c8e)"></div>
    <h4>Various renewables offered</h4><p>Lorem ipsum dolor sit amet, consectetur adipi scin.</p>
    <div class="btn">READ MORE</div>
  </article>
  <article class="card" style="left:460px">
    <div class="ph" role="img" aria-label="Wind turbines in a field at sunrise" style="background:linear-gradient(180deg,#4f86d6,#c9d3dc 60%,#a48c6a)"></div>
    <h4>Energy Saving Assessment</h4><p>Lorem ipsum dolor sit amet, consectetur adipi scin.</p>
    <div class="btn">READ MORE</div>
  </article>
  <article class="card" style="left:770px">
    <div class="ph" role="img" aria-label="Business meeting with model wind turbines on a table" style="background:linear-gradient(180deg,#cfd5da,#8d9aa5 60%,#e9ecef)"></div>
    <h4>Monitoring</h4><p>Lorem ipsum dolor sit amet, consectetur adipi scin.</p>
    <div class="btn">READ MORE</div>
  </article>
</section>

<footer>
  <div class="abs footer"></div>
  <h3 class="f-h" style="left:150px">CONATCT US</h3>
  <h3 class="f-h" style="left:494px">LINKS</h3>
  <div class="f-item" style="top:3830px"><span class="f-ic"><svg width="18" height="18" viewBox="0 0 24 24"><path fill="#fff" d="M6.6 10.8a15 15 0 0 0 6.6 6.6l2.2-2.2c.3-.3.7-.4 1-.2 1.1.4 2.3.6 3.6.6.6 0 1 .4 1 1V20c0 .6-.4 1-1 1A17 17 0 0 1 3 4c0-.6.4-1 1-1h3.5c.6 0 1 .4 1 1 0 1.3.2 2.5.6 3.6.1.3 0 .7-.2 1z"/></svg></span><span>Phone<br>+00 5550 1942</span></div>
  <div class="f-item" style="top:3897px"><span class="f-ic"><svg width="18" height="14" viewBox="0 0 18 14"><rect width="18" height="14" rx="2" fill="#fff"/><path d="M1 1l8 7 8-7" stroke="#1f78e6" stroke-width="2" fill="none"/></svg></span><span>Email<br>hello@korvoenergy.com</span></div>
  <div class="f-item" style="top:3972px"><span class="f-ic"><svg width="16" height="22" viewBox="0 0 16 22"><path fill="#fff" d="M8 0a8 8 0 0 1 8 8c0 6-8 14-8 14S0 14 0 8a8 8 0 0 1 8-8z"/><circle cx="8" cy="8" r="3" fill="#1f78e6"/></svg></span><span>Brindle Row 8,<br>4410 Aldmere</span></div>
  <div class="abs f-links">Home<br>About us<br>Services Offer<br>Renewable Solutions<br>Contact us<br>Terms and Conditions<br>Privacy policy</div>
  <div class="abs f-brand">KORVO RENEWABLES</div>
  <div class="abs socials" aria-label="Social media links"><span></span><span></span><span></span></div>
  <p class="abs copy">Copyright © 2022 All Right Reserved</p>
</footer>

</body>
</html>
```